High Tech Real Estate Startup needs a business card

We are developing an innovative real estate marketing product based around advanced search and virtual reality.

We talk to people, we need business cards.

Target Market(s)

The target market is technology professionals and realtors.

Contact Information for Business Card

The information to be included will include

Name
Title
Phone Number
E-mail Address
www.quelzo.com

It should use simple iconography for each one of those fields.

Font styles to use
Other font styles liked:
• Co, Jubilat, Avenir

Colors

Designer to choose colors to be used in the design.

Requirements
Must have
• Clean aesthetic,
• Good use of negative space.
• It should use our company logo, shown in the attached file. It is able to use the negative of that logo (coloured font and white background) and I have attached other acceptable accent colours in a swatch file.
Should not have
• Should not be too busy
• No extraneous text (slogans, tag lines etc)

```html
<!DOCTYPE html>
<html lang="en">
<head>
<meta charset="utf-8">
<title>Quelzo Business Card</title>
<link rel="stylesheet" href="https://fonts.googleapis.com/css2?family=Nunito+Sans:wght@400;600&display=swap">
<style>
  :root {
    --teal: #08b8be;
    --white: #ffffff;
    --ink: #1b2628;
    --backdrop: #e9eded;
  }
  * { margin: 0; padding: 0; box-sizing: border-box; }
  html, body { width: 1200px; height: 901px; overflow: hidden; }
  body {
    background: var(--backdrop);
    font-family: "Nunito Sans", "Helvetica Neue", Arial, sans-serif;
    position: relative;
  }
  .card {
    position: absolute;
    left: 240px;
    width: 720px;
    height: 411px;
    background: var(--teal);
    color: var(--white);
    overflow: hidden;
  }
  .card--front { top: 26px; }
  .card--back { top: 464px; }

  .company-name {
    position: absolute;
    font-family: "Nunito Sans", "Helvetica Neue", Arial, sans-serif;
    font-weight: 600;
    color: var(--white);
    line-height: 1;
    white-space: nowrap;
  }
  .card--front .company-name {
    font-size: 104px;
    left: 0;
    right: 40px;
    top: 150px;
    text-align: center;
  }
  .card--back .company-name {
    font-size: 62px;
    right: 44px;
    top: 42px;
  }

  .holder {
    position: absolute;
    left: 0;
    top: 150px;
  }
  .holder__bar {
    position: absolute;
    left: 0;
    top: 6px;
    width: 16px;
    height: 56px;
    background: var(--white);
  }
  .holder__name {
    margin-left: 48px;
    font-size: 34px;
    font-weight: 400;
    color: var(--ink);
    line-height: 1.1;
  }
  .holder__title {
    margin-left: 48px;
    font-size: 18px;
    font-weight: 600;
    color: var(--white);
  }
  .contact {
    position: absolute;
    left: 140px;
    top: 262px;
    font-size: 18px;
    line-height: 1.3;
  }
  .contact__address { margin-bottom: 6px; }
  .contact__list { list-style: none; }
  .contact__item {
    display: flex;
    align-items: center;
    gap: 12px;
    height: 27px;
  }
  .contact__icon { width: 18px; height: 18px; flex: none; }
</style>
</head>
<body>
  <section class="card card--front">
    <div class="company-name">QUELZO</div>
  </section>

  <section class="card card--back">
    <div class="company-name">QUELZO</div>
    <div class="holder">
      <span class="holder__bar"></span>
      <p class="holder__name">Nadia Ferrow</p>
      <p class="holder__title">Director</p>
    </div>
    <div class="contact">
      <p class="contact__address">Suite 4 - 118 Harlow Parade<br>Kestrel Bay QLD 4571</p>
      <ul class="contact__list">
        <li class="contact__item">
          <svg class="contact__icon" viewBox="0 0 20 20" aria-hidden="true">
            <circle cx="10" cy="10" r="8.5" fill="none" stroke="#fff" stroke-width="1.6"/>
            <path d="M7 5.5l1.6 2.4-1 1.1c.6 1.3 1.4 2.1 2.6 2.7l1.1-1 2.4 1.5-.8 1.8c-3.5-.3-6.5-3.4-6.8-6.8z" fill="#fff"/>
          </svg>
          <span>063829175</span>
        </li>
        <li class="contact__item">
          <svg class="contact__icon" viewBox="0 0 20 20" aria-hidden="true">
            <rect x="1.5" y="4" width="17" height="12" fill="none" stroke="#fff" stroke-width="1.6"/>
            <path d="M1.5 4l8.5 7 8.5-7M1.5 16l6-5.5M18.5 16l-6-5.5" fill="none" stroke="#fff" stroke-width="1.4"/>
          </svg>
          <span>info@youremail.com</span>
        </li>
        <li class="contact__item">
          <svg class="contact__icon" viewBox="0 0 20 20" aria-hidden="true">
            <circle cx="10" cy="10" r="8.5" fill="none" stroke="#fff" stroke-width="1.6"/>
            <path d="M1.5 10h17M10 1.5c-3 3-3 14 0 17M10 1.5c3 3 3 14 0 17M3.5 5.5h13M3.5 14.5h13" fill="none" stroke="#fff" stroke-width="1.2"/>
          </svg>
          <span>www.quelzo.com</span>
        </li>
      </ul>
    </div>
  </section>
</body>
</html>
```